New Business Card Design Project

Hi! I would like for you to design a business card for our aesthetic injections business. We offer Zelvia, filler, skin care. I would like it to be elegant, feminine, modern and sleek/clean. I like black/gold foil/ivory/parchment colors. It can be either one or two sided. I would like matte black with gold foil logo on one side and ivory with gold foil information on the other side

Target Market(s)

target market is the discerning woman who wants to look her best

Industry/Entity Type

beauty

Contact Information for Business Card

logo, name, phone, email, website, instagram, facebook, location

Requirements
Must have
• logo and info
Nice to have
• the icons for cell, instagram, email, fb etc
Should not have
• images of people

```html
<!DOCTYPE html>
<html lang="en">
<head>
<meta charset="UTF-8">
<title>Velour Studio – Business Card</title>
<link rel="stylesheet" href="https://fonts.googleapis.com/css2?family=Montserrat:wght@400;500;700&display=swap">
<style>
  :root {
    --backdrop: #1d1d1d;
    --matte-black: #0f0f10;
    --ivory: #f8f1da;
    --gold: #c8982c;
    --gold-light: #d9ab3d;
  }
  * { box-sizing: border-box; margin: 0; padding: 0; }
  html, body {
    width: 1200px;
    height: 1200px;
    overflow: hidden;
    background: var(--backdrop);
    font-family: "Montserrat", sans-serif;
  }
  .canvas {
    position: relative;
    width: 1200px;
    height: 1200px;
  }
  .card {
    position: absolute;
    left: 150px;
    width: 900px;
    height: 514px;
    border-radius: 26px;
  }
  .card--front {
    top: 66px;
    background: var(--matte-black);
    display: flex;
    align-items: center;
    justify-content: center;
  }
  .card--back {
    top: 620px;
    background: var(--ivory);
    color: var(--gold);
  }
  .brand {
    display: flex;
    align-items: center;
    gap: 22px;
    color: var(--gold-light);
    font-weight: 500;
    letter-spacing: 0.28em;
    text-transform: uppercase;
  }
  .brand__dot {
    flex: none;
    border: 1.5px solid currentColor;
    border-radius: 50%;
  }
  .brand--large { font-size: 40px; }
  .brand--large .brand__dot { width: 34px; height: 34px; }
  .brand--small {
    position: absolute;
    right: 60px;
    top: 200px;
    font-size: 20px;
    gap: 12px;
    color: var(--gold);
  }
  .brand--small .brand__dot { width: 18px; height: 18px; }
  .holder {
    position: absolute;
    left: 64px;
    top: 62px;
  }
  .holder__name {
    font-size: 30px;
    font-weight: 700;
    letter-spacing: 0.08em;
    text-transform: uppercase;
  }
  .holder__title {
    font-size: 22px;
    font-weight: 400;
    letter-spacing: 0.06em;
    text-transform: uppercase;
    margin-top: 4px;
  }
  .contact {
    position: absolute;
    left: 64px;
    bottom: 62px;
    font-size: 22px;
    font-weight: 400;
    letter-spacing: 0.1em;
    line-height: 1.6;
  }
</style>
</head>
<body>
  <main class="canvas">
    <section class="card card--front">
      <div class="brand brand--large">
        <span class="brand__dot"></span>
        <span class="brand__name">Velour Studio</span>
      </div>
    </section>

    <section class="card card--back">
      <div class="holder">
        <p class="holder__name">Marcus Hale</p>
        <p class="holder__title">CEO/Founder</p>
      </div>

      <div class="brand brand--small">
        <span class="brand__dot"></span>
        <span class="brand__name">Velour Studio</span>
      </div>

      <div class="contact">
        <p class="contact__line">P : 555-013-2046 &nbsp;|&nbsp; E : hello@velourstudio.com</p>
        <p class="contact__line">www.velourstudio.com</p>
      </div>
    </section>
  </main>
</body>
</html>
```